NEW Household Invention Needs a Package Design!

We need a 'retail' package design for a new product invented for the household kitchen market. Tiverlyn has developed a reusable food storage system that can be tailored to an individual's needs and have a sustainable impact on their ability to make good dietary decisions, while helping save the planet. We would like to see designs that use the brand's branding guidelines and logo. The final design should communicate the key features of the product (patented customizable modular system, fill lines, collapsible functionality and sustainable materials), as well as, all other notable aspects (Microwave/Dishwasher Safe, Leakproof, 100% BPA Free, Donates 1% of purchase price, etc.). It's important that the benefits of the product are well highlighted (More variety to better balance nutrition, More easily stored in bag, kitchen cabinet or drawer and Ends waste)
Updates

Hi All, we are looking for a package design for retail, something that will be on a shelf in our product category.

Need extra days to review

Target Market(s)

Health conscious men and women who have a passion for nutrition & social responsibility, operate a lifestyle on-the-go and monitor their spending by preparing meals at home.

Industry/Entity Type

Food Tech, Consumer Products, Health & Wellness

Font styles to use
Other font styles liked:
• See Brand Guidelines

Requirements
Must have
• Follow brand guidelines: https://guidelines.morbexcreative.com/tiverlyn/guidelines/

```html
<!DOCTYPE html>
<html lang="en">
<head>
<meta charset="utf-8">
<title>Tiverlyn – The Mosaic container set</title>
<link rel="stylesheet" href="https://fonts.googleapis.com/css2?family=Work+Sans:wght@400;600;700&display=swap">
<style>
  :root {
    --kraft: #c7b08b;
    --kraft-dark: #bda57f;
    --sky: #a6d7f3;
    --sky-light: #cfe9f8;
    --sky-deep: #86c6ec;
    --lid: #eef7fc;
    --plum: #821d62;
    --white: #ffffff;
    --page: #ffffff;
  }
  * { margin: 0; padding: 0; box-sizing: border-box; }
  html, body {
    width: 1200px; height: 831px; overflow: hidden;
    background: var(--page);
    font-family: "Work Sans", Arial, sans-serif;
  }
  .sleeve {
    position: absolute; left: 398px; top: 57px;
    width: 403px; height: 717px;
    background: linear-gradient(160deg, var(--kraft) 0%, var(--kraft-dark) 100%);
    color: var(--white);
  }
  .brand-name {
    position: absolute; left: 22px; top: 30px;
    font-weight: 700; font-size: 58px; letter-spacing: -1.5px; line-height: 1;
  }
  .product-title {
    position: absolute; left: 27px; top: 160px;
    font-weight: 700; font-size: 48px; line-height: 1; letter-spacing: -0.5px;
  }
  .product-subtitle {
    position: absolute; left: 27px; top: 209px;
    font-weight: 700; font-size: 19px; line-height: 1;
  }
  .tagline {
    position: absolute; left: 27px; top: 236px;
    font-weight: 600; font-size: 9.6px; line-height: 1.25;
  }
  .product-photo {
    position: absolute; left: 0; top: 280px; width: 403px; height: 285px;
    background:
      radial-gradient(ellipse 38% 30% at 52% 40%, var(--lid) 0%, rgba(238,247,252,0) 100%),
      radial-gradient(ellipse 30% 26% at 72% 62%, var(--lid) 0%, rgba(238,247,252,0) 100%),
      radial-gradient(ellipse 28% 20% at 30% 75%, var(--sky-light) 0%, rgba(207,233,248,0) 100%),
      linear-gradient(180deg, var(--sky) 0%, var(--sky-deep) 100%);
  }
  .seal {
    position: absolute; left: 275px; top: 233px;
    width: 96px; height: 96px; border-radius: 50%;
    background: var(--plum);
    display: flex; align-items: center; justify-content: center;
    font-weight: 700; font-size: 16px; color: var(--white);
  }
  .features {
    position: absolute; left: 202px; top: 606px;
    display: flex; gap: 10px;
  }
  .feature {
    width: 48px; height: 81px;
    border: 1px solid var(--white); border-radius: 4px;
    display: flex; flex-direction: column; align-items: center;
  }
  .feature svg { margin-top: 10px; }
  .feature-label {
    margin-top: auto; margin-bottom: 6px;
    font-size: 6.8px; line-height: 1.2; text-align: center; font-weight: 400;
  }
</style>
</head>
<body>
  <main class="sleeve">
    <div class="brand-name">tiverlyn</div>
    <h1 class="product-title">The Mosaic</h1>
    <h2 class="product-subtitle">container set</h2>
    <p class="tagline">The ideal lunchbox for the on-the-go lifestyle.<br>Pack a balanced meal, perfectly portioned.</p>

    <div class="product-photo" role="img" aria-label="Product photo: modular collapsible blue silicone containers with clear snap lids and fill lines, one holding sliced bread and tomato, one holding salad, plus a collapsed container"></div>

    <div class="seal">tiverlyn</div>

    <section class="features">
      <div class="feature">
        <svg width="26" height="18" viewBox="0 0 26 18" fill="none" stroke="#fff" stroke-width="0.8">
          <rect x="0.5" y="0.5" width="25" height="17"/>
          <rect x="3" y="3" width="14" height="12"/>
          <path d="M8 7c1 1-1 2 0 4M10 7c1 1-1 2 0 4M12 7c1 1-1 2 0 4"/>
          <rect x="19.5" y="3" width="4" height="2.5"/>
          <rect x="19.5" y="7" width="4" height="2.5"/>
          <rect x="19.5" y="11" width="4" height="2.5"/>
        </svg>
        <div class="feature-label">Microwave/<br>Dishwasher<br>Safe</div>
      </div>
      <div class="feature">
        <svg width="34" height="32" viewBox="0 0 34 32" fill="none" stroke="#fff" stroke-width="0.8">
          <path d="M14 8c-3 5-5 7-5 10a5 5 0 0 0 10 0c0-3-2-5-5-10z"/>
          <path d="M21 18c-1.5 2.5-2.5 3.5-2.5 5a2.5 2.5 0 0 0 5 0c0-1.5-1-2.5-2.5-5z"/>
          <path d="M2 31L32 1"/>
        </svg>
        <div class="feature-label">Leakproof</div>
      </div>
      <div class="feature">
        <svg width="22" height="20" viewBox="0 0 22 20" fill="none" stroke="#fff" stroke-width="0.8">
          <path d="M3 18C2 9 9 2 20 2c0 10-6 16-15 15z"/>
          <path d="M1 19L15 7M8 13h5M10 11V7"/>
        </svg>
        <div class="feature-label">100%<br>BPA<br>Free</div>
      </div>
    </section>
  </main>
</body>
</html>
```